Silverpine Orbit Works Flyer

We need a one page promotional piece that explains what our company does, and the benefits it provides in a simple, elegant, easy to understand way. I would like to print it on glossy heavyweight paper to give a feel of high quality and legitimacy. I will include the logo, the tag line, and the main benefits that the company offers.

Tag line concept, may not need these exact words. "Lend us 5 minutes each morning, and we will guide you toward a Silverpine Orbit Works."

Key points...(exact wording not required if you think of a better way to say it)

Software easy enough for my grandpa to use.
Lets you use snail mail, email, texting, and social media to quickly market to your customers at very low cost.
Web based which allows you to launch media campaigns from your desktop, or smartphone in moments.
Quick 3 - 5 minute training videos which give you hard hitting, quick action tips that will help you make your business better today.
Live coaching calls to help motivate you to improve your business.
No contracts, or start up fees. One low price of $299 per month.

Restaurant owners

Restaurant

```html
<!DOCTYPE html>
<html lang="en">
<head>
<meta charset="utf-8">
<title>Silverpine Orbit Works Flyer</title>
<link rel="stylesheet" href="https://fonts.googleapis.com/css2?family=Roboto+Condensed:wght@700&display=swap">
<style>
  :root {
    --paper: #ffffff;
    --ink: #6a6a6a;
    --ink-dark: #3c3c3c;
    --accent: #6b9b2c;
    --bar: #1c1c1c;
    --bar-text: #ffffff;
    --rule: #2a2a2a;
    --mark: #b9b9b9;
    --watermark: #f4f4f4;
  }
  * { margin: 0; padding: 0; box-sizing: border-box; }
  html, body { width: 849px; height: 1200px; overflow: hidden; background: var(--paper); }
  .flyer {
    position: relative;
    width: 849px;
    height: 1200px;
    overflow: hidden;
    background: var(--paper);
    font-family: "Roboto Condensed", "Arial Narrow", sans-serif;
    font-weight: 700;
    color: var(--ink);
    text-align: center;
  }
  .backdrop-disc {
    position: absolute;
    left: 124px;
    top: 560px;
    width: 600px;
    height: 600px;
    border-radius: 50%;
    background: var(--watermark);
  }
  .brand {
    position: absolute;
    top: 86px;
    left: 0;
    width: 100%;
  }
  .brand-disc {
    display: block;
    width: 170px;
    height: 170px;
    margin: 0 auto;
    border-radius: 50%;
    background: var(--mark);
  }
  .brand-name {
    margin-top: 34px;
    font-size: 44px;
    line-height: 1;
    color: var(--ink-dark);
    letter-spacing: 0.5px;
  }
  .tagline {
    position: absolute;
    top: 401px;
    left: 0;
    width: 100%;
    font-size: 27px;
    line-height: 38px;
    white-space: nowrap;
  }
  .divider {
    position: absolute;
    top: 494px;
    left: 120px;
    width: 612px;
    height: 2px;
    background: var(--rule);
  }
  .benefits {
    position: absolute;
    top: 517px;
    left: 0;
    width: 100%;
    list-style: none;
    font-size: 27px;
    line-height: 40px;
    white-space: nowrap;
  }
  .benefits li { margin-bottom: 22px; }
  .accent { color: var(--accent); }
  .offer-bar {
    position: absolute;
    top: 1033px;
    left: 57px;
    width: 738px;
    height: 48px;
    background: var(--bar);
    color: var(--bar-text);
    font-size: 27px;
    line-height: 48px;
    white-space: nowrap;
    border-radius: 3px;
  }
</style>
</head>
<body>
<main class="flyer">
  <div class="backdrop-disc" aria-hidden="true"></div>

  <header class="brand">
    <span class="brand-disc" aria-hidden="true"></span>
    <h1 class="brand-name">Silverpine Orbit Works</h1>
  </header>

  <p class="tagline">Lend us 5 minutes each morning, and we will guide you<br>toward a Silverpine <span class="accent">Orbit</span> Works.</p>

  <div class="divider" aria-hidden="true"></div>

  <ul class="benefits">
    <li>Software <span class="accent">easy</span> enough for my grandpa to use.</li>
    <li>Lets you use snail mail, email, texting, and social media<br>to quickly market to your customers at <span class="accent">very low cost</span>.</li>
    <li>Web based which allows you to launch media campaigns<br>from your desktop, or smartphone <span class="accent">in moments</span>.</li>
    <li>Quick 3 - 5 minute training videos which give you hard<br>hitting, quick action tips that will help you<br><span class="accent">make your business better today</span>.</li>
    <li>Live coaching calls to help motivate you<br>to <span class="accent">improve your business</span>.</li>
  </ul>

  <p class="offer-bar">No contracts or start up fees. One low price of $299 per month.</p>
</main>
</body>
</html>
```